5 Slice cake label for 6 products

Will be using printed film to upgrade a packet of cakes.
There will be 6 varieties of same product, please see page 5 in leaflet attached.
Jam & Coconut, Lemon, Cherry, Chocolate Chip, Double Chocolate Chip, Angel.

Current images attached, need to freshen up.

More modern for today's marketplace.

Product will be sold in retail outlets across the UK

Target Market(s)

Shoppers buying in supermarkets

Industry/Entity Type

Product

Font styles to use
Sans Serif

Requirements
Must have
• Colourful, digital mocked up images. Easy on the eye. Each product to have suitable colours.
• LABEL MUST COVER ALL OF PACKET
Nice to have
• Attractiveness
Should not have
• Be too crowded or messy. SHOULD NOT LOOK LIKE A LABEL.
• Must show all details

```html
<!DOCTYPE html>
<html lang="en">
<head>
<meta charset="utf-8">
<title>Jam &amp; Coconut – 5 Slice Cake Label</title>
<link rel="stylesheet" href="https://fonts.googleapis.com/css2?family=Questrial&display=swap">
<style>
  :root {
    --page: #ffffff;
    --band-orange: #f7941d;
    --band-orange-soft: #f58a22;
    --band-brown: #b3401b;
    --band-red: #ac2e19;
    --band-red-soft: #a82a17;
    --badge-cream: #f6ead8;
    --badge-orange: #ee5a28;
    --badge-core: #b0421b;
    --white: #ffffff;
  }
  * { margin: 0; padding: 0; box-sizing: border-box; }
  html, body {
    width: 1200px;
    height: 1000px;
    overflow: hidden;
    background: var(--page);
  }
  .label {
    position: absolute;
    left: 40px;
    top: 210px;
    width: 1120px;
    height: 580px;
    overflow: hidden;
    font-family: "Questrial", sans-serif;
    color: var(--white);
  }
  .band { position: absolute; left: 0; width: 100%; }
  .band--top {
    top: 0; height: 234px;
    background: linear-gradient(180deg, var(--band-orange), var(--band-orange-soft));
  }
  .band--middle {
    top: 234px; height: 91px;
    background: var(--band-brown);
    box-shadow: 0 2px 6px rgba(0,0,0,0.25);
  }
  .band--bottom {
    top: 325px; height: 255px;
    background: linear-gradient(180deg, var(--band-red), var(--band-red-soft));
  }
  .tagline {
    position: absolute;
    left: 422px;
    top: 267px;
    font-size: 20.5px;
    line-height: 26px;
    white-space: nowrap;
  }
  .badge {
    position: absolute;
    left: 38px;
    top: 115px;
    width: 368px;
    height: 368px;
    border-radius: 50%;
    background: radial-gradient(circle, var(--badge-orange) 0 168px, var(--badge-cream) 170px);
    box-shadow: 0 3px 8px rgba(0,0,0,0.3);
  }
  .badge-core {
    position: absolute;
    left: 86px;
    top: 163px;
    width: 272px;
    height: 272px;
    border-radius: 50%;
    background: var(--badge-core);
    border: 2px solid var(--white);
  }
  .badge-line {
    position: absolute;
    left: 86px;
    width: 272px;
    text-align: center;
    font-weight: 400;
    white-space: nowrap;
    transform: translateY(-50%);
  }
  .badge-line--first { top: 240px; font-size: 48px; }
  .badge-line--second { top: 307px; font-size: 48px; }
  .badge-line--count { top: 366px; font-size: 25px; }
  .brand-name {
    position: absolute;
    left: 102px;
    top: 96px;
    width: 240px;
    text-align: center;
    font-size: 20px;
    letter-spacing: 1px;
  }
</style>
</head>
<body>
  <main class="label">
    <div class="band band--top" role="img" aria-label="Orange band with a fine diamond lattice pattern"></div>
    <div class="band band--middle"></div>
    <div class="band band--bottom" role="img" aria-label="Deep red band with a faint diamond lattice pattern"></div>

    <p class="tagline">maderiea cake slices topped&nbsp; with mixed fruit jam &amp; desiccated coconut</p>

    <div class="badge" role="img" aria-label="Scalloped rosette badge with cream edge and stitched orange ring"></div>
    <div class="badge-core"></div>
    <h1>
      <span class="badge-line badge-line--first">Jam</span>
      <span class="badge-line badge-line--second">&amp;&nbsp; Coconut</span>
    </h1>
    <p class="badge-line badge-line--count">5 Slice</p>

    <p class="brand-name">Crumb &amp; Co</p>
  </main>
</body>
</html>
```